Business Card, A4 Letter Head and DL Envelope for Vantrelle

We are looking for a design for our Business Card, A4 Letter Head and DL Envelope.

Vantrelle is a distributor of promotional products. We specialize in a range of branded promotional products, these include pens, polo shirts, key rings, drink bottles, uniforms and bags to name a few. We are experts in marketing and assist companies in choosing the right promotional product for their needs. We will predominately be an online business where customers visit our website and browse our range of promotional products and branding options.

Our colours are black, red, white and grey.

Files must be supplied in eps, pdf and ai format.

Please display the following information:
Corbin Hale
Account Manager
Suite xxx, 214 Dawlish Parade Melbourne, Victoria 3000
Phone +61 3 5550 1827
Mobile +61 455 501 936
sales@vantrelle.com.au
www.vantrelle.com.au

```html
<!DOCTYPE html>
<html lang="en">
<head>
<meta charset="utf-8">
<title>Vantrelle Business Card</title>
<link rel="stylesheet" href="https://fonts.googleapis.com/css2?family=Open+Sans:wght@400;600;700&display=swap">
<style>
  :root {
    --backdrop: #3a3a3a;
    --card-white: #ffffff;
    --brand-red: #e2001a;
    --brand-red-dark: #c20018;
    --silver-light: #ececec;
    --silver-mid: #d2d2d2;
    --silver-dark: #a4a4a4;
    --ink-dark: #3b3b3b;
    --ink-grey: #6e6e6e;
    --ink-body: #5a5a5a;
  }
  * { box-sizing: border-box; margin: 0; padding: 0; }
  html, body {
    width: 1200px; height: 441px; overflow: hidden;
    background: var(--backdrop);
    font-family: "Open Sans", Arial, sans-serif;
  }
  .card {
    position: absolute; top: 67px;
    width: 527px; height: 306px;
    overflow: hidden;
  }
  .card--front { left: 51px; }
  .card--back { left: 606px; background: var(--card-white); }
  .card__artwork {
    position: absolute; inset: 0;
    background: linear-gradient(120deg,
      var(--brand-red) 0%,
      var(--brand-red-dark) 22%,
      var(--silver-light) 48%,
      var(--silver-mid) 75%,
      var(--silver-dark) 100%);
  }
  .brand {
    position: absolute; left: 268px; top: 246px;
    font-size: 24px; font-weight: 700; letter-spacing: 0.6px;
    color: var(--ink-dark);
  }
  .contact { position: absolute; left: 22px; top: 32px; color: var(--ink-body); }
  .contact__name {
    font-size: 20px; font-weight: 400; color: var(--ink-dark);
    letter-spacing: 0.3px; line-height: 1.15;
  }
  .contact__role {
    font-size: 14px; color: var(--ink-grey); letter-spacing: 0.3px;
  }
  .contact__block { font-size: 14.5px; line-height: 1.45; margin-top: 14px; }
  .contact__block--address { margin-top: 51px; }
  .contact__web { color: var(--brand-red); }
</style>
</head>
<body>
  <section class="card card--front" aria-label="Card front">
    <div class="card__artwork" role="img" aria-label="Decorative red and silver background artwork"></div>
    <div class="brand">VANTRELLE</div>
  </section>

  <section class="card card--back" aria-label="Card back">
    <div class="contact">
      <h1 class="contact__name">CORBIN HALE</h1>
      <p class="contact__role">ACCOUNT MANAGER</p>
      <p class="contact__block contact__block--address">Suite xxx, 214 Dawlish Parade Melbourne,<br>Victoria 3000</p>
      <p class="contact__block">Phone +61 3 5550 1827<br>Mobile +61 455 501 936</p>
      <p class="contact__block">sales@vantrelle.com.au<br><span class="contact__web">www.vantrelle.com.au</span></p>
    </div>
  </section>
</body>
</html>
```